Design and upgrade professional label for the agricultural market

We are Keltra The Green Acre and need an upgrade of our existing label. We are a professional b2b company that focuses on natural solutions for farms (cattle, crops,...). This is also what the label should be looking like. I attached existing labels that need an upgrade, we would like to see similar branding, so our customers will still recognise our company and an upgrade in professional look. Fonts, colors (also of the logo), can change and are free to choose. Attached also a document that explains all the elements that need to be on the label.

Target Market(s)

Natural agricultural market worldwilde/farmers/b2b market

Industry/Entity Type

Agriculture

Font styles to use
Sans Serif

Requirements
Must have
• Photo of product purpose, professional font, professional colors, b2b market

```html
<!DOCTYPE html>
<html lang="nl">
<head>
<meta charset="utf-8">
<title>Ademhalingsondersteuning – Koe en Kalf label</title>
<link href="https://fonts.googleapis.com/css2?family=Source+Sans+3:wght@300;400;600;700;800&display=swap" rel="stylesheet">
<style>
  :root {
    --brand-blue: #2349b8;
    --heading-blue: #1f3a9e;
    --brand-green: #5cb840;
    --body-grey: #9a9a9a;
    --danger-red: #e8192c;
    --ink: #222;
    --paper: #ffffff;
  }
  * { margin: 0; padding: 0; box-sizing: border-box; }
  html, body { width: 1200px; height: 875px; overflow: hidden; background: #ececec; }
  body { font-family: "Source Sans 3", sans-serif; }
  .label { position: relative; width: 1200px; height: 875px; background: var(--paper); }
  .abs { position: absolute; }

  .title-band { left: 0; top: 53px; width: 517px; height: 148px; background: var(--brand-blue); color: #fff; }
  .title-line1 { position: absolute; left: 37px; top: 28px; font-size: 24px; font-weight: 700; letter-spacing: 5.2px; white-space: nowrap; }
  .title-line2 { position: absolute; left: 37px; top: 64px; font-size: 48px; font-weight: 800; letter-spacing: 9px; white-space: nowrap; }

  .hero-photo { left: 0; top: 215px; width: 517px; height: 513px;
    background: linear-gradient(180deg, #c9d4dc 0%, #5d6f6a 22%, #34503f 48%, #4c6a33 70%, #7a9a3c 85%, #5f7a34 100%); }

  .danger-box { left: 36px; top: 747px; width: 347px; height: 91px; border: 1.5px solid var(--danger-red); }
  .danger-head { background: var(--danger-red); color: #fff; font-size: 13px; font-weight: 700; padding: 1px 7px; height: 20px; line-height: 18px; }
  .danger-text { font-size: 5.6px; line-height: 8.4px; color: var(--ink); padding: 3px 7px; }
  .pictogram { top: 766px; width: 54px; height: 54px; }

  .brand-box { left: 541px; top: 54px; width: 142px; height: 147px; border: 3px solid var(--brand-green);
    display: flex; flex-direction: column; justify-content: center; align-items: center; text-align: center; }
  .brand-name { font-size: 25px; font-weight: 700; color: var(--heading-blue); line-height: 1.05; }

  .address { left: 953px; top: 77px; width: 229px; height: 89px; border-top: 1px solid var(--brand-green); border-bottom: 1px solid var(--brand-green); }
  .address-title { text-align: center; font-size: 11px; font-weight: 700; color: var(--brand-green); height: 18px; line-height: 18px; border-bottom: 1px solid var(--brand-green); }
  .address-row { position: absolute; font-size: 6.8px; line-height: 9.6px; color: var(--ink); }
  .address-row svg { position: absolute; }

  .section-head { left: 538px; width: 644px; font-size: 14px; font-weight: 700; color: var(--heading-blue); border-bottom: 1px solid var(--heading-blue); line-height: 16px; padding-left: 3px; }
  .body-text { left: 538px; width: 644px; font-size: 12.6px; line-height: 13.7px; font-weight: 300; color: var(--body-grey); }
  .usp-list { left: 538px; top: 232px; list-style: none; font-size: 14.6px; font-weight: 300; color: var(--body-grey); line-height: 21.5px; }
  .tick { color: var(--brand-green); font-weight: 600; margin-right: 5px; }
  .tagline { left: 538px; top: 316px; font-size: 20px; font-weight: 600; color: var(--brand-green); }
  .instructions { left: 538px; top: 504px; font-size: 12.4px; font-weight: 300; color: var(--body-grey); line-height: 17.4px; }
  .instructions b { font-weight: 600; color: var(--heading-blue); }
  .instructions .g { color: var(--brand-green); font-weight: 400; }

  .remarks { left: 538px; top: 750px; font-size: 12px; color: var(--body-grey); line-height: 25px; }
  .remarks b { color: var(--heading-blue); font-weight: 700; }
  .remarks .g { color: var(--brand-green); }
  .badge { top: 747px; width: 48px; height: 48px; border-radius: 50%; }
  .footer-rule { left: 538px; top: 801px; width: 644px; border-top: 1px solid var(--heading-blue); }
  .footer { left: 538px; top: 811px; width: 644px; display: flex; justify-content: space-between; font-size: 11px; color: var(--body-grey); }
  .footer span b { color: var(--heading-blue); font-weight: 400; }
</style>
</head>
<body>
<div class="label">

  <div class="abs title-band">
    <div class="title-line1">ADEMHALINGSONDERSTEUNING</div>
    <div class="title-line2">– KOEENKALF</div>
  </div>

  <div class="abs hero-photo" role="img" aria-label="Photo of a cow and suckling calf on a green alpine meadow with mountains behind"></div>

  <div class="abs danger-box">
    <div class="danger-head">Dangersentences</div>
    <p class="danger-text">Schadelijk bij inslikken. Veroorzaakt ernstige brandwonden en oogletsel. Na het werken met dit product handen, onderarmen en gezicht grondig wassen. Draag beschermende handschoenen, beschermende kleding, oogbescherming, gelaatsbescherming. NA INSLIKKEN: de mond spoelen — GEEN braken opwekken. Onmiddellijk een ANTIGIFCENTRUM, een arts raadplegen. BIJ CONTACT MET DE HUID (of het haar): verontreinigde kleding onmiddellijk uittrekken. Huid met water afspoelen/afdouchen. Onmiddellijk een ANTIGIFCENTRUM, een arts raadplegen. BIJ CONTACT MET DE OGEN: voorzichtig afspoelen met water gedurende een aantal minuten; contactlenzen verwijderen, indien mogelijk; blijven spoelen. Onmiddellijk een arts, een ANTIGIFCENTRUM raadplegen. Bevat: Mierenzuur 48%.</p>
  </div>

  <svg class="abs pictogram" style="left:395px" viewBox="0 0 54 54" role="img" aria-label="Corrosive hazard pictogram">
    <path d="M27 3 L51 27 L27 51 L3 27 Z" fill="#fff" stroke="#e8192c" stroke-width="3.5"/>
    <rect x="16" y="30" width="22" height="4" fill="#222"/>
  </svg>
  <svg class="abs pictogram" style="left:452px" viewBox="0 0 54 54" role="img" aria-label="Exclamation hazard pictogram">
    <path d="M27 3 L51 27 L27 51 L3 27 Z" fill="#fff" stroke="#e8192c" stroke-width="3.5"/>
    <path d="M24.5 14 H29.5 L28.5 32 H25.5 Z" fill="#111"/>
    <circle cx="27" cy="37" r="2.8" fill="#111"/>
  </svg>

  <div class="abs brand-box">
    <div class="brand-name">Keltra<br>The Green<br>Acre</div>
  </div>

  <div class="abs address">
    <div class="address-title">COMPANY ADDRESS</div>
    <div class="address-row" style="left:6px;top:25px">
      <svg width="12" height="12" viewBox="0 0 12 12" style="left:0;top:0"><path d="M6 1 L11.5 6 H10 V11 H7 V8 H5 V11 H2 V6 H0.5 Z" fill="#2349b8"/></svg>
      <div style="position:absolute;left:21px;white-space:nowrap">Keltra Laboratories Int. B.V.<br>Akkerveldlaan 47<br>5912 KR Veldhoven (NL)</div>
      <div style="position:absolute;left:133px;white-space:nowrap">Keltra Laboratories NV<br>Molenbeekstraat<br>88 bus 14</div>
    </div>
    <div class="address-row" style="left:6px;top:64px">
      <svg width="12" height="14" viewBox="0 0 12 14" style="left:0;top:1px"><path d="M3 1 L5 4 L4 6 C4.5 8 6 9.5 8 10 L10 9 L11.5 11.5 L9.5 13 C5 12.5 1 8 1 3 Z" fill="#2349b8"/></svg>
      <div style="position:absolute;left:20px;white-space:nowrap">+31 400 12 77 90<br>+32 10 45 62 30</div>
      <svg width="13" height="9" viewBox="0 0 13 9" style="left:100px;top:4px"><rect x="0.5" y="0.5" width="12" height="8" fill="none" stroke="#2349b8"/><path d="M0.5 0.5 L6.5 5 L12.5 0.5 M0.5 8.5 L5 4 M12.5 8.5 L8 4" fill="none" stroke="#2349b8"/></svg>
      <div style="position:absolute;left:120px;top:4px;white-space:nowrap">hello@keltragreenacre.com</div>
    </div>
  </div>

  <div class="abs section-head" style="top:219px">Product USP’s:</div>
  <ul class="abs usp-list">
    <li><span class="tick">✓</span>Ondersteunt de dieren in perioden van stress, lusteloosheid of zwakte</li>
    <li><span class="tick">✓</span>Ondersteunt de conditie en het natuurlijke afweersysteem</li>
    <li><span class="tick">✓</span>Stimuleert het ademhalingsstelsel</li>
  </ul>

  <div class="abs tagline">Voor een optimale ondersteuning van de luchtwegen</div>

  <div class="abs section-head" style="top:362px">Product description</div>
  <p class="abs body-text" style="top:382px">Ademhalingsondersteuning – Koe en Kalf is een voormengsel voor runderen en kalveren. Het is een vloeibare premix op basis van kruiden- en vruchtenextracten en organische zuren. Ademhalingsondersteuning – Koe en Kalf zorgt voor een optimale ondersteuning van de conditie van de luchtwegen van koeien en kalveren. De conditie van het ademhalingsstelsel is bepalend voor een goede gezondheid en productie en wordt o.a. beïnvloed door het rantsoen, de infectiedruk en de algehele weerstand. Het product voorkomt snot, slijm, slijmvlies en longproblemen en draagt daardoor bij aan een optimaal welzijn en een efficiënte productie.</p>

  <div class="abs section-head" style="top:483px">User instructions</div>
  <div class="abs instructions">
    <div><b>Voor koeien:</b> het product 1 tot 2 maal daags 10 ml per dier in het voer of het drinkwater mengen.</div>
    <div><b>Voor kalveren:</b> het product 1 tot 2 maal daags 5 ml per dier in het voer of het drinkwater mengen.</div>
    <div><span class="g">✓ Bij perioden van verminderde weerstand:</span> tot 4 dagen lang de dubbele dossering toepassen.</div>
    <div><span class="g">✓ Bij kuur:</span> 10 dagen lang de normale hoeveelheid doseren, 10 dagen niet, dan weer 10 dagen wel.</div>
  </div>

  <div class="abs section-head" style="top:589px">Composition</div>
  <p class="abs body-text" style="top:609px">Appel-, bieten-, vlierbessenwijn, Achillea Millefolium, Hypericum Perforatum, Echinacea Purpureae, Thymus Vulgaris, Primula veris, Plantago Lanceolata, Harpagophytum Procumbens, Urtica Urens, Potentilla Tormentilla, Ribes Nigrum, Capsella Bursa Pastoris, Spirea Ulmaria, Mentha Piperita, Salvia Officinalis, Calendula Officinalis, Foeniculum Vulgare, Alchemilla Vulgaris, Trifolii Pratense, Taraxacum, EleutrococcusSenticosus, Verbascum Thapsus, Luzerne Medicago Sativa, Vaccinum Myrtillus.</p>

  <div class="abs section-head" style="top:695px">Analytical constituents</div>
  <p class="abs body-text" style="top:714px">1% Ruw eiwit, 1% ruwe celstof, 1% ruw vet, 1% ruwe as, 0.5% lysine 0.5% methionine, 0.05% natrium.</p>

  <div class="abs remarks">
    <div><b>Remarks:-</b> Kort schudden voor gebruik.</div>
    <div><b>GMP+FSA assured.Registration nr.</b> : GMP027613.</div>
  </div>

  <div class="abs badge" style="left:824px;background:var(--heading-blue)" role="img" aria-label="Origin certificate badge"></div>
  <div class="abs badge" style="left:879px;background:var(--brand-green)" role="img" aria-label="Ecological certificate badge"></div>
  <div class="abs badge" style="left:934px;background:#3a6fc4" role="img" aria-label="Quality certificate badge"></div>

  <div class="abs footer-rule"></div>
  <div class="abs footer">
    <span><b>LABEL NUMBER</b> : 130422</span>
    <span><b>BEST BEFORE</b> : SEE PACKAGING</span>
    <span><b>BATCH NUMBER</b> : SEE PACKAGING</span>
    <span><b>NET VOLUME</b> : SEE PACKAGING</span>
  </div>

</div>
</body>
</html>
```